Letterhead PT. Bima Raya Lestari Developer

Alo , My Company need a letterhead design for PT. Bima Raya Lestari Developer Real Estate , i need your each other creative design letterhead for my PT.Bima Raya Lestari Developer Real Estate guys
input my data in letterhead :
Address : Komp. Ruko Taman Sari Blok F No. 27
No. Telp : 0778 512 3364 / 0812 4395 7716
Email : bimarayalestari@mailbox-example.com
Website : www.bimarayalestari-example.com

Target Market(s)

Buyer Property Real Estate & Investor

Industry/Entity Type

Real Estate Development

Font styles to use
Serif
Sans Serif

Requirements
Must have
• according to your creative each other guys as long i need
• Address : Komp. Ruko Taman Sari Blok F No. 27
• No. Telp : 0778 512 3364 / 0812 4395 7716
• Email : bimarayalestari@mailbox-example.com
• Website : www.bimarayalestari-example.com
Nice to have
Should not have
• don't want another colour except : white , dark blue n gold suit to our logo developer real estate

```html
<!DOCTYPE html>
<html lang="id">
<head>
<meta charset="utf-8">
<title>Letterhead — PT. Bima Raya Lestari Developer</title>
<link href="https://fonts.googleapis.com/css2?family=Open+Sans:wght@400;600;700&display=swap" rel="stylesheet">
<style>
  :root {
    --navy: #13305a;
    --gold: #c6872f;
    --paper: #ffffff;
    --backdrop: #e9e9ea;
    --ink-soft: #2b3447;
  }
  * { margin: 0; padding: 0; box-sizing: border-box; }
  html, body {
    width: 1200px; height: 795px; overflow: hidden;
    background: var(--backdrop);
    font-family: "Open Sans", Arial, sans-serif;
  }
  .letterhead {
    position: absolute;
    left: 339px; top: 27px;
    width: 523px; height: 740px;
    background: var(--paper);
    box-shadow: 0 2px 10px rgba(0,0,0,0.08);
    overflow: hidden;
  }
  .brand {
    position: absolute; left: 42px; top: 52px;
    display: flex; align-items: center; gap: 8px;
  }
  .brand-mark {
    width: 12px; height: 12px; background: var(--navy);
  }
  .brand-name {
    color: var(--navy);
    font-weight: 700; font-size: 11.5px;
    letter-spacing: 0.3px; text-transform: uppercase;
    line-height: 1.2; max-width: 150px;
  }
  .contact {
    position: absolute; right: 36px; top: 44px;
    list-style: none;
    color: var(--ink-soft);
    font-size: 7.5px; line-height: 1.6;
  }
  .contact li { display: flex; align-items: center; gap: 5px; }
  .contact svg { width: 7px; height: 7px; fill: var(--navy); flex: none; }
  .footer-band {
    position: absolute; left: 0; bottom: 0;
    width: 523px; height: 70px;
  }
  .website {
    position: absolute; right: 18px; bottom: 11px;
    color: #fff; font-size: 9px; font-weight: 600; letter-spacing: 0.3px;
    line-height: 12px; white-space: nowrap;
  }
</style>
</head>
<body>
  <main class="letterhead">
    <header class="brand">
      <span class="brand-mark"></span>
      <span class="brand-name">PT. Bima Raya Lestari Developer</span>
    </header>

    <ul class="contact">
      <li>
        <svg viewBox="0 0 10 10"><path d="M5 0 L10 5 H8.5 V10 H6 V7 H4 V10 H1.5 V5 H0 Z"/></svg>
        Komp. Ruko Taman Sari Blok F No. 27
      </li>
      <li>
        <svg viewBox="0 0 10 10"><path d="M2 0 L4 2.5 L3 4 Q4.5 6 6 7 L7.5 6 L10 8 L8.5 10 Q3 9 0 1.5 Z"/></svg>
        0778 512 3364 / 0812 4395 7716
      </li>
      <li>
        <svg viewBox="0 0 10 10"><path d="M0 2 H10 V8 H0 Z M0 2 L5 5.5 L10 2" stroke="#fff" stroke-width="0.8"/></svg>
        bimarayalestari@mailbox-example.com
      </li>
    </ul>

    <svg class="footer-band" viewBox="0 0 523 70" aria-hidden="true">
      <path d="M0 54 H280 Q292 54 300 44 Q308 36 320 36 H523 V70 H0 Z" fill="var(--navy)"/>
      <path d="M0 49 H276 Q288 49 296 39 Q304 31 316 31 H523" fill="none" stroke="var(--gold)" stroke-width="3"/>
    </svg>
    <span class="website">www.bimarayalestari-example.com</span>
  </main>
</body>
</html>
```